Small Artisan Bakery Needs a new Bread Bag Label

I'm looking for a new bread bag label design for our artisan bakery. I have attached photos of our current logo (we will be using this in the label) and pictures of our bread bag. For this project we will focus on one of our bread (100% Rye) however I would like the final final to be in a format I can edit for other bread types.

We are thinking that each bread bag will have 2 labels, our logo on top of the bread bag window (as shown in the attached photos) and simple bread description below the window.

We typically use Copperplate font however we are open to ideas as long as it keeps in alignment with our logo.

*Also note, we will not be printing the labels directly on the bag. The designs will be printed as labels that will be stuck on each bag. I would like to have the final designs formatted in a way that makes it simple to have printed at a standard printing shop.

The bag is 9.5" long, 5" wide.

The length fro the bottom of the bag window to the bottom of the bag is 2".

Top of the bag to top of the window is a little over 4".

Since these labels will be printed on label paper and manually stuck on the bag I would like them to not be take up up the whole space above or below the bag window. If the label design comes to the edge of the bag it will be very difficult to physically stick the label on the bag straight.

Thanks

Hi, The bag is 9.5" long, 5" wide. The length fro the bottom of the bag window to the bottom of the bag is 2". Top of the bag to top of the window is a little over 4". Since these labels will be printed on label paper and manually stuck on the bag I would like them to not be take up up the whole space above or below the bag window. If the label design comes to the edge of the bag it will be very difficult to physically stick the label on the bag straight. Thanks

```html
<!DOCTYPE html>
<html lang="en">
<head>
<meta charset="utf-8">
<title>Birch Creek Bread – Rye Bag Labels</title>
<link rel="stylesheet" href="https://fonts.googleapis.com/css2?family=Cinzel:wght@700&family=Arimo:wght@700&display=swap">
<style>
  :root {
    --label-brown: #3e2317;
    --label-ink: #f4ede4;
    --page-bg: #ffffff;
  }
  html, body {
    margin: 0;
    padding: 0;
    width: 1200px;
    height: 1033px;
    overflow: hidden;
    background: var(--page-bg);
  }
  .canvas {
    position: relative;
    width: 1200px;
    height: 1033px;
  }
  .label {
    position: absolute;
    left: 323px;
    display: block;
  }
  .label--brand { top: 55px; }
  .label--ingredients { top: 754px; }
  .label-body { fill: var(--label-brown); }
  .label-rule {
    fill: none;
    stroke: var(--label-ink);
    stroke-width: 2.5;
  }
  .brand-name {
    font-family: "Cinzel", serif;
    font-weight: 700;
    fill: var(--label-ink);
    letter-spacing: 2px;
  }
  .product-title {
    font-family: "Cinzel", serif;
    font-weight: 700;
    font-size: 50px;
    fill: var(--label-ink);
  }
  .product-note,
  .ingredient-line {
    font-family: "Arimo", sans-serif;
    font-weight: 700;
    fill: var(--label-ink);
  }
  .product-note { font-size: 25px; }
  .ingredients-heading {
    font-family: "Arimo", sans-serif;
    font-weight: 700;
    font-size: 29px;
    fill: var(--label-ink);
    letter-spacing: 1px;
  }
  .ingredient-line { font-size: 21px; }
  .ink-dot { fill: var(--label-ink); }
</style>
</head>
<body>
<main class="canvas">

  <svg class="label label--brand" width="554" height="653" viewBox="0 0 554 653" aria-label="Birch Creek Bread rye bread label">
    <rect class="label-body" x="0" y="0" width="554" height="653" rx="26"/>
    <rect class="label-rule" x="13" y="13" width="528" height="627" rx="16"/>
    <path class="label-rule" d="M13 70 C13 230 80 264 277 264 C474 264 541 230 541 70"/>

    <circle class="ink-dot" cx="277" cy="60" r="12"/>
    <text class="brand-name" x="277" y="138" text-anchor="middle" font-size="44">BIRCH CREEK</text>
    <text class="brand-name" x="277" y="196" text-anchor="middle" font-size="44">BREAD</text>

    <text class="product-title" x="277" y="356" text-anchor="middle">100% RYE BREAD</text>
    <line class="label-rule" x1="92" y1="386" x2="255" y2="386"/>
    <line class="label-rule" x1="299" y1="386" x2="462" y2="386"/>
    <circle class="ink-dot" cx="277" cy="386" r="8" role="img" aria-label="small ornament between rules"/>

    <text class="product-note" x="277" y="449" text-anchor="middle">NATURALLY LEAVENED</text>
    <text class="product-note" x="277" y="486" text-anchor="middle">AND FERMENTED</text>
    <text class="product-note" x="277" y="541" text-anchor="middle">100% LITHUANIAN</text>
    <text class="product-note" x="277" y="576" text-anchor="middle">RYE BREAD</text>
  </svg>

  <svg class="label label--ingredients" width="554" height="224" viewBox="0 0 554 224" aria-label="Ingredients label">
    <rect class="label-body" x="0" y="0" width="554" height="224" rx="24"/>
    <rect class="label-rule" x="13" y="13" width="528" height="198" rx="14"/>
    <circle class="ink-dot" cx="45" cy="112" r="9"/>
    <circle class="ink-dot" cx="509" cy="112" r="9"/>

    <text class="ingredients-heading" x="277" y="62" text-anchor="middle">INGREDIENTS</text>
    <text class="ingredient-line" x="277" y="96" text-anchor="middle">100% ORGANIC RYE FLOUR</text>
    <text class="ingredient-line" x="277" y="124" text-anchor="middle">110 YEAR OLD ORGANIC</text>
    <text class="ingredient-line" x="277" y="152" text-anchor="middle">RYE CULTURE</text>
    <text class="ingredient-line" x="277" y="180" text-anchor="middle">GREY CELTIC SALT</text>
  </svg>

</main>
</body>
</html>
```